Boutique Shoe Bag Race wear Business Card Design

We are a new luxury shoe bag, jewellery and race wear store stocking local and international designers. Located in the fashion precinct of beautiful Larkspur Bay famous in Sydney Australia. Stocking French jewellery and shoes such as Maximilien verdacs plus Australian made. Looking at quality and service and looking after the locals and tourists.
Ideas: White background, Black writing in bold engravers, logo in middle of Bondi and Boutique a gold horseshoe (facing upright so the curve is at the bottom) with a black stiletto inside. French clover silver and black border (not irish clover the French lattice type look)

Larkspur Parlour

I open 8/4 so require business card design ASAP.

Please place gold horseshoe facing upwards with the black stiletto inside.

Bold engravers writing for business name.

I will have my phone number tomorrow to update.

Border in similar/same style as attached picture with black/silver clover French design.

Thank you. Petra                                   

Industry/Entity Type

Fashion

Contact Information for Business Card

Larkspur Parlour
Boutique Owner Petra Halvorsen
41B Tindle Road
Larkspur Bay NSW 2197 Australia
0491237406
02 **** *TBA
info@larkspurparlour.com.au
Pagefolio.com/LarkspurParlour
www.larkspurparlour.com.au

Font styles to use
Other font styles liked:
• Bold Engravers

Requirements
Must have
• Info on one side including business name and logo with black stiletto and gold horse shoe. reverse side with French clover border and Larger name Larkspur Parlour with logo in centre.
Should not have
• irish clover
French script
horseshoe upside down

```html
<!DOCTYPE html>
<html lang="en">
<head>
<meta charset="utf-8">
<title>Larkspur Parlour – Business Cards</title>
<link rel="stylesheet" href="https://fonts.googleapis.com/css2?family=Questrial&family=Outfit:wght@600&display=swap">
<style>
  :root {
    --backdrop: #ece9e4;
    --card-white: #ffffff;
    --ink: #1c1c1c;
    --ink-soft: #2e2e2e;
    --lattice-dark: #1f1f21;
    --lattice-mid: #3a3a3d;
    --silver-light: #e4e4e4;
    --silver-dark: #9a9a9a;
    --gold: #b8862f;
    --icon-grey: #8a8a8a;
  }
  * { box-sizing: border-box; margin: 0; padding: 0; }
  html, body {
    width: 1200px; height: 1000px; overflow: hidden;
    background: var(--backdrop);
    font-family: "Questrial", "Century Gothic", sans-serif;
    color: var(--ink);
  }
  .canvas { position: relative; width: 1200px; height: 1000px; }

  .card {
    position: absolute;
    width: 660px; height: 400px;
    box-shadow: 0 6px 18px rgba(0,0,0,0.18);
  }

  /* Reverse side: lattice border */
  .card--reverse { left: 70px; top: 60px; }
  .lattice-border {
    position: absolute; inset: 0;
    background: radial-gradient(circle at 40% 35%, var(--lattice-mid), var(--lattice-dark) 75%);
  }
  .reverse-panel {
    position: absolute; inset: 44px;
    background: var(--card-white);
    display: flex; flex-direction: column; align-items: center; justify-content: center;
  }
  .brand-mark { display: flex; align-items: center; gap: 18px; margin-top: -10px; }
  .brand-mark__dot {
    width: 26px; height: 26px; border-radius: 50%;
    background: var(--gold);
  }
  .brand-mark__name {
    font-size: 56px; font-weight: 400; color: var(--ink); letter-spacing: 0.5px;
  }
  .reverse-url {
    position: absolute; bottom: 14px; left: 0; right: 0;
    text-align: center; font-size: 21px; color: var(--ink-soft);
  }

  /* Front side: contact details */
  .card--front { left: 470px; top: 540px; }
  .silver-frame {
    position: absolute; inset: 0;
    background: linear-gradient(135deg, var(--silver-dark), var(--silver-light) 45%, var(--silver-dark) 100%);
  }
  .front-panel {
    position: absolute; inset: 16px;
    background: var(--card-white);
  }
  .front-brand {
    position: absolute; left: 34px; top: 24px;
    font-size: 46px; font-weight: 400; color: var(--ink);
  }
  .front-dot {
    position: absolute; right: 58px; top: 84px;
    width: 56px; height: 56px; border-radius: 50%;
    background: var(--gold);
  }
  .owner { position: absolute; left: 36px; top: 150px; }
  .owner__name {
    font-family: "Outfit", "Century Gothic", sans-serif;
    font-weight: 600; font-size: 28px; line-height: 34px; color: var(--ink);
  }
  .owner__role { font-size: 28px; line-height: 34px; color: var(--ink-soft); }

  .contact-list { position: absolute; left: 30px; bottom: 26px; list-style: none; }
  .contact-list li {
    display: flex; align-items: center; gap: 6px;
    font-size: 21px; line-height: 28px; color: var(--ink-soft); white-space: nowrap;
  }
  .contact-list svg { width: 20px; height: 20px; flex: none; }
  .social-dot {
    width: 18px; height: 18px; border-radius: 50%;
    background: var(--icon-grey); flex: none; margin-right: 2px;
  }

  .address {
    position: absolute; right: 26px; bottom: 26px;
    font-style: normal; text-align: right;
    font-size: 21px; line-height: 28px; color: var(--ink-soft); white-space: nowrap;
  }
</style>
</head>
<body>
<main class="canvas">

  <section class="card card--reverse" aria-label="Business card reverse">
    <div class="lattice-border" role="img" aria-label="Black and silver French lattice pattern border"></div>
    <div class="reverse-panel">
      <div class="brand-mark">
        <span class="brand-mark__name">Larkspur Parlour</span>
        <span class="brand-mark__dot"></span>
      </div>
      <p class="reverse-url">www.larkspurparlour.com.au</p>
    </div>
  </section>

  <section class="card card--front" aria-label="Business card front">
    <div class="silver-frame"></div>
    <div class="front-panel">
      <h1 class="front-brand">Larkspur Parlour</h1>
      <span class="front-dot"></span>

      <div class="owner">
        <p class="owner__name">Petra Halvorsen</p>
        <p class="owner__role">Boutique Owner</p>
      </div>

      <ul class="contact-list">
        <li>
          <svg viewBox="0 0 20 20" aria-hidden="true"><rect x="6" y="2" width="8" height="16" rx="1.5" fill="none" stroke="#8a8a8a" stroke-width="1.4"/><line x1="9" y1="15.5" x2="11" y2="15.5" stroke="#8a8a8a" stroke-width="1.4"/></svg>
          0491237406 02
        </li>
        <li>
          <svg viewBox="0 0 20 20" aria-hidden="true"><rect x="2" y="5" width="16" height="11" fill="none" stroke="#8a8a8a" stroke-width="1.4"/><polyline points="2,5 10,11 18,5" fill="none" stroke="#8a8a8a" stroke-width="1.4"/></svg>
          info@larkspurparlour.com.au
        </li>
        <li>
          <span class="social-dot"></span>
          Pagefolio.com/LarkspurParlour
        </li>
      </ul>

      <address class="address">
        41B Tindle Road<br>
        Larkspur Bay<br>
        NSW 2197 Australia
      </address>
    </div>
  </section>

</main>
</body>
</html>
```